New Word Template Design Project

I want design about template plant date palm tree
The size is A4/Users/mibu/Desktop/DSC07540.JPG
/Users/mibu/Desktop/DSC07514.JPG

```html
<!DOCTYPE html>
<html lang="en">
<head>
<meta charset="utf-8">
<title>Date Palm Document Template</title>
<link rel="stylesheet" href="https://fonts.googleapis.com/css2?family=Arimo:wght@400;700&family=Oswald:wght@500&display=swap">
<style>
  :root {
    --leaf-green: #84b341;
    --logo-green: #3a9a4a;
    --ink: #111111;
    --paper: #ffffff;
    --slate: #8a8b8d;
  }
  * { margin: 0; padding: 0; box-sizing: border-box; }
  html, body { width: 849px; height: 1200px; overflow: hidden; background: var(--paper); }
  .page {
    position: relative;
    width: 849px;
    height: 1200px;
    font-family: "Arimo", Helvetica, Arial, sans-serif;
    color: var(--ink);
    overflow: hidden;
  }
  .brand-name {
    position: absolute;
    left: 70px;
    top: 50px;
    font-size: 16.5px;
    font-weight: 700;
    color: var(--logo-green);
    letter-spacing: 0.1px;
  }
  .site-address {
    position: absolute;
    right: 70px;
    top: 50px;
    font-size: 16.5px;
    font-weight: 700;
  }
  .page-title {
    position: absolute;
    left: 67px;
    top: 215px;
    font-size: 53px;
    line-height: 1;
    font-weight: 700;
    color: var(--leaf-green);
    letter-spacing: -0.3px;
  }
  .lead {
    position: absolute;
    left: 69px;
    top: 286px;
    width: 730px;
    font-size: 25px;
    line-height: 36px;
  }
  .body-column {
    position: absolute;
    top: 593px;
    width: 345px;
    font-size: 14.6px;
    line-height: 18.85px;
  }
  .body-column p + p { margin-top: 15px; }
  .column-left { left: 70px; }
  .column-right { left: 442px; }
  .footer-band {
    position: absolute;
    left: 0;
    top: 1139px;
    width: 849px;
    height: 61px;
    background: var(--leaf-green);
  }
  .footer-label {
    position: absolute;
    right: 86px;
    top: 11px;
    font-family: "Oswald", "Arial Narrow", sans-serif;
    font-weight: 500;
    font-size: 17px;
    color: var(--paper);
    letter-spacing: 0.3px;
  }
  .page-number {
    position: absolute;
    right: 0;
    top: 0;
    width: 61px;
    height: 61px;
    background: var(--slate);
    color: var(--paper);
    font-weight: 700;
    font-size: 16px;
    display: flex;
    align-items: center;
    justify-content: center;
    padding-bottom: 6px;
  }
</style>
</head>
<body>
<div class="page">
  <header>
    <div class="brand-name">YOUR LOGO HERE</div>
    <div class="site-address">www.dategrove.com</div>
  </header>

  <h1 class="page-title">Your Title Goes Here</h1>

  <p class="lead">Lorem ipsum dolor sit amet, consectetur adipiscing elit. Fusce ut consequat nulla. Etiam in tincidunt elit. Sed semper tristique erat. Pellentesque quis vulputate eros. Fusce euismod ultricies nunc vel tempus. Vivamus semper congue erat et finibus. Aenean ut mollis lectus. Duis et est luctus, rutrum magna non, fermentum quam. Fusce condimentum varius libero. Sed purus turpis, lobortis non est fringilla.</p>

  <section class="body-column column-left">
    <p>Lorem ipsum dolor sit amet, consectetur adipiscing elit. Fusce ut consequat nulla. Etiam in tincidunt elit. Sed semper tristique erat. Pellentesque quis vulputate eros. Fusce euismod ultricies nunc vel tempus. Vivamus semper congue erat et finibus. Aenean ut mollis lectus. Duis et est luctus, rutrum magna non, fermentum quam. Fusce condimentum varius libero. Sed purus turpis, lobortis non est fringilla, blandit hendrerit enim. Suspendisse tempus consectetur risus et rhoncus. Aliquam a ipsum in arcu varius porta sit amet id elit.</p>
    <p>Phasellus eget odio sodales, suscipit odio at, luctus felis. Donec rhoncus sagittis finibus. Class aptent taciti sociosqu ad litora torquent per conubia nostra, per inceptos himenaeos. Integer quis felis at justo aliquet volutpat. Praesent bibendum neque quis euismod mollis. Class aptent taciti sociosqu ad litora torquent per conubia nostra, per inceptos himenaeos. Praesent in turpis id nisi eleifend porttitor. Duis sed urna felis. Integer mattis mattis leo, non sollicitudin est feugiat vitae. Proin nibh quam, cursus nec leo non, hendrerit convallis mauris. In ullamcorper justo sed ligula tristique lacinia. Nulla at ultricies lorem, id egestas arcu.</p>
  </section>

  <section class="body-column column-right">
    <p>Lorem ipsum dolor sit amet, consectetur adipiscing elit. Fusce ut consequat nulla. Etiam in tincidunt elit. Sed semper tristique erat. Pellentesque quis vulputate eros. Fusce euismod ultricies nunc vel tempus. Vivamus semper congue erat et finibus. Aenean ut mollis lectus. Duis et est luctus, rutrum magna non, fermentum quam. Fusce condimentum varius libero. Sed purus turpis, lobortis non est fringilla, blandit hendrerit enim. Suspendisse tempus consectetur risus et rhoncus. Aliquam a ipsum in arcu varius porta sit amet id elit.</p>
    <p>Phasellus eget odio sodales, suscipit odio at, luctus felis. Donec rhoncus sagittis finibus. Class aptent taciti sociosqu ad litora torquent per conubia nostra, per inceptos himenaeos. Integer quis felis at justo aliquet volutpat. Praesent bibendum neque quis euismod mollis. Class aptent taciti sociosqu ad litora torquent per conubia nostra, per inceptos himenaeos. Praesent in turpis id nisi eleifend porttitor. Duis sed urna felis. Integer mattis mattis leo, non sollicitudin est feugiat vitae. Proin nibh quam, cursus nec leo non, hendrerit convallis mauris. In ullamcorper justo sed ligula tristique lacinia. Nulla at ultricies lorem, id egestas arcu.</p>
  </section>

  <footer class="footer-band">
    <span class="footer-label">LOREM IPSUM DOLOR SIT AMET</span>
    <span class="page-number">3</span>
  </footer>
</div>
</body>
</html>
```